Hollow Briar Flower Shop Jumbo Postcard

We are opening a new flower shop in a small southern town. Our style is a bit different than the traditional flower shop. We are specializing in garden wild floral bouquets and arrangements. We will offer a frequent flower program, roses for a month promotion. We are offering a free gift with any in store purchase. We are looking for a design that reflects our logo and its' colors and the focus on using foraged and natural elements in our work. We want to provide a product that stands out from the rest and that grabs your attention and makes people ask where did that come from?? We will supply flowers for all occasions, event planning, and one of a kind home décor items. We will have special start up offers of free local delivery to the first 30 customers mentioning the postcard offer, and special flower happy hour specials each day week. Finally I want to convey that we are new, we are different, and ready to serve our local community. We love rustic and shabby chic designs. . I want to postcard offers to stand out and grab the recipients' attention. It should include our contact info and website, what we provide, and our tagline from the business card.
Industry/Entity Type
Floral

```html
<!DOCTYPE html>
<html lang="en">
<head>
<meta charset="utf-8">
<title>Hollow Briar Flower Shop Postcard</title>
<link rel="stylesheet" href="https://fonts.googleapis.com/css2?family=Della+Respira&family=Courgette&display=swap">
<style>
  :root {
    --cream: #fefee0;
    --mint: #6fdfb4;
    --mint-edge: #86d8b0;
    --tan: #f2dc9e;
    --tan-deep: #dcc37f;
    --orange: #e8946a;
    --orange-light: #f0a77a;
    --purple: #4b2f86;
    --ink: #4a3a7a;
    --white: #ffffff;
  }
  html, body {
    margin: 0;
    padding: 0;
    width: 1200px;
    height: 923px;
    overflow: hidden;
    background: var(--cream);
  }
  .postcard {
    position: relative;
    width: 1200px;
    height: 923px;
    background: var(--cream);
  }
  .postcard-shapes {
    position: absolute;
    inset: 0;
  }
  .tagline {
    position: absolute;
    left: 30px;
    top: 18px;
    width: 520px;
    margin: 0;
    text-align: center;
    font-family: "Della Respira", serif;
    font-weight: 400;
    font-size: 31px;
    line-height: 48px;
    color: var(--white);
  }
  .brand-name {
    position: absolute;
    left: 166px;
    top: 212px;
    width: 220px;
    text-align: center;
    font-family: "Della Respira", serif;
    font-weight: 400;
    color: var(--purple);
    margin: 0;
  }
  .brand-name .brand-main {
    display: block;
    font-size: 40px;
    line-height: 42px;
  }
  .brand-name .brand-sub {
    display: block;
    font-size: 15px;
    letter-spacing: 3px;
    text-transform: uppercase;
    margin-top: 6px;
  }
  .contact-tag {
    position: absolute;
    left: -6px;
    top: 390px;
    width: 400px;
    height: 122px;
    border-radius: 6px;
    background: linear-gradient(180deg, var(--orange-light), var(--orange));
    box-shadow: 0 2px 4px rgba(120, 70, 40, 0.25);
    transform: rotate(-4deg);
    transform-origin: left top;
  }
  .contact-tag address {
    font-style: normal;
    font-family: "Della Respira", serif;
    font-size: 25px;
    line-height: 40px;
    color: var(--purple);
    padding: 8px 0 0 30px;
  }
  .offer-text {
    position: absolute;
    left: 345px;
    top: 565px;
    width: 235px;
    margin: 0;
    text-align: center;
    font-family: "Courgette", cursive;
    font-weight: 400;
    font-size: 25px;
    line-height: 38px;
    color: var(--purple);
  }
  .postage-box {
    position: absolute;
    left: 975px;
    top: 75px;
    width: 136px;
    height: 136px;
    border: 2px solid var(--ink);
    display: flex;
    align-items: center;
    justify-content: center;
    text-align: center;
    font-family: Arial, Helvetica, sans-serif;
    font-size: 22px;
    line-height: 29px;
    color: var(--ink);
  }
  .address-lines {
    position: absolute;
    left: 695px;
    top: 440px;
    width: 406px;
    margin: 0;
    padding: 0;
    list-style: none;
  }
  .address-lines li {
    height: 69px;
    border-top: 2px solid var(--ink);
  }
</style>
</head>
<body>
<main class="postcard">
  <svg class="postcard-shapes" width="1200" height="923" viewBox="0 0 1200 923">
    <defs>
      <linearGradient id="bloom-tones" x1="0" y1="0" x2="1" y2="1">
        <stop offset="0" stop-color="#f08a5d"/>
        <stop offset="0.55" stop-color="#8fd8b0"/>
        <stop offset="1" stop-color="#5b3a9a"/>
      </linearGradient>
      <clipPath id="panel-clip">
        <rect x="0" y="100" width="570" height="638"/>
      </clipPath>
    </defs>

    <rect class="panel-tan" x="0" y="100" width="570" height="638" fill="var(--tan)"/>
    <path class="panel-tab" d="M0,737 H170 C140,737 132,780 100,780 H0 Z" fill="var(--tan)"/>
    <path class="tagline-band" d="M0,0 H570 V115 H170 C140,115 132,158 100,158 H0 Z" fill="var(--mint)"/>
    <rect class="panel-edge" x="570" y="0" width="7" height="742" fill="var(--mint-edge)"/>

    <g clip-path="url(#panel-clip)">
      <circle class="offer-badge" cx="478" cy="640" r="143" fill="var(--tan-deep)" stroke="var(--mint-edge)" stroke-width="4"/>
      <rect role="img" aria-label="Small wildflower cluster in the badge corner" x="530" y="702" width="40" height="36" rx="16" fill="url(#bloom-tones)" opacity="0.7"/>
    </g>
    <rect role="img" aria-label="Wildflower cluster with orange and purple blooms above the offer" x="362" y="478" width="130" height="80" rx="36" fill="url(#bloom-tones)" opacity="0.7"/>

    <circle class="logo-disc" cx="276" cy="262" r="124" fill="var(--white)" stroke="var(--mint-edge)" stroke-width="5"/>
    <rect role="img" aria-label="Wildflower cluster with orange and purple blooms on the upper right of the logo disc" x="245" y="106" width="200" height="98" rx="44" fill="url(#bloom-tones)" opacity="0.7"/>
    <rect role="img" aria-label="Wildflower cluster with orange and purple blooms on the lower left of the logo disc" x="134" y="324" width="160" height="58" rx="26" fill="url(#bloom-tones)" opacity="0.7"/>
  </svg>

  <p class="tagline">Specialized in garden wild floral bouquets and arrangements.</p>

  <h1 class="brand-name">
    <span class="brand-main">Hollow<br>Briar</span>
    <span class="brand-sub">Flower Shop</span>
  </h1>

  <div class="contact-tag">
    <address>4180, Magnolia Ln. Suite C,<br>Pinecrest, La 70512<br>337 555 0192</address>
  </div>

  <p class="offer-text">Get<br>a free gift<br>with any in store<br>purchase.</p>

  <div class="postage-box">Postage<br>Area</div>

  <ul class="address-lines">
    <li></li>
    <li></li>
    <li></li>
    <li></li>
  </ul>
</main>
</body>
</html>
```